Web design for Modeling agency

We are looking for re-designing our modeling agency website.
Current website: lunafaces.com our competitor: KTRfaces.com
http://brisaface.fr/
https://www.corvelmanagement.com/models/
https://www.hedwig-faces.de
https://www.rustmanagement.co.uk
https://www.quorbfaces.com
https://www.harborlightfaces.com

Target Market(s)

modeling agency

Industry/Entity Type

modeling agency

Number of Pages Required

5+ page

Font styles to use
Other font styles liked:
• base on logo guidline

Requirements
Nice to have
• current website: lunafaces.com our competitor: KTRfaces.com

```html
<!DOCTYPE html>
<html lang="en">
<head>
<meta charset="utf-8">
<title>Luna Faces — Menu</title>
<link href="https://fonts.googleapis.com/css2?family=Cormorant+Garamond:wght@400;500&family=Questrial&family=Tinos&display=swap" rel="stylesheet">
<style>
  :root {
    --backdrop: #e6e6e6;
    --page: #ffffff;
    --brand: #b08a6e;
    --ink: #5e5a58;
    --ink-soft: #6d6866;
    --rule: #ececec;
    --overlay-dark: #8a8a8a;
    --overlay-light: #cfcfcf;
    --coral: #f0875a;
    --coral-deep: #e2764a;
    --next-btn: #f7a985;
    --dropdown: rgba(240, 170, 150, 0.82);
  }
  * { margin: 0; padding: 0; box-sizing: border-box; }
  html, body {
    width: 1200px; height: 720px; overflow: hidden;
    background: var(--backdrop);
    font-family: "Questrial", sans-serif;
  }
  .page {
    position: absolute; left: 86px; top: 69px; width: 1021px; height: 572px;
    background: var(--page);
    box-shadow: 0 8px 28px rgba(0,0,0,0.28);
    overflow: hidden;
  }
  .grid-lines { position: absolute; inset: 0; }
  .abs { position: absolute; }

  .menu-panel {
    left: 69px; top: 57px; width: 408px; height: 471px;
    background: radial-gradient(ellipse at 35% 45%, var(--overlay-light) 0%, #a9a9a9 45%, var(--overlay-dark) 75%, rgba(255,255,255,0.6) 100%);
    filter: blur(2px);
  }
  .menu-fade {
    left: 69px; top: 40px; width: 420px; height: 500px;
    background: linear-gradient(to right, rgba(255,255,255,0) 70%, #fff 100%),
                linear-gradient(to bottom, #fff 0%, rgba(255,255,255,0) 8%, rgba(255,255,255,0) 90%, #fff 100%);
  }
  .close-btn { left: 74px; top: 28px; width: 14px; height: 14px; }

  .city-list {
    left: 141px; top: 61px; display: flex; align-items: center;
    font-family: "Tinos", serif; font-size: 10px; color: var(--ink);
  }
  .city-list span { padding: 0 4px; line-height: 13px; }
  .city-list span + span { border-left: 1px solid var(--ink); }
  .city-list .current { color: #fff; font-size: 11px; }

  .main-menu {
    left: 69px; top: 116px; width: 408px; list-style: none; text-align: center;
  }
  .main-menu li {
    position: absolute; left: 0; width: 100%;
    font-size: 15.5px; letter-spacing: 0.3px; color: var(--ink-soft);
  }
  .main-menu .active { color: #fff; font-size: 17px; }
  .main-menu .active span { padding: 0 8px 4px; border-bottom: 1px solid #fff; }

  .brand {
    left: 476px; top: 20px; font-family: "Cormorant Garamond", serif;
    font-size: 32px; font-weight: 400; color: var(--brand); letter-spacing: -1px;
  }
  .top-nav { font-size: 8px; color: var(--ink); top: 34px; letter-spacing: 0.2px; }
  .search {
    left: 886px; top: 32px; width: 64px; height: 13px;
    border: 1px solid #ececec; border-radius: 7px;
  }
  .search svg { position: absolute; right: 6px; top: 2px; }

  .photo-mono {
    left: 477px; top: 61px; width: 177px; height: 448px;
    background: linear-gradient(180deg, #f2f2f2 0%, #d6d6d6 38%, #8d8d8d 62%, #5b5b5b 100%);
  }
  .photo-colour {
    left: 654px; top: 61px; width: 300px; height: 448px;
    background: radial-gradient(ellipse at 55% 55%, #3f4a35 0%, #4d5a40 28%, var(--coral-deep) 55%, var(--coral) 100%);
  }
  .lang-menu {
    left: 829px; top: 61px; width: 52px; height: 41px;
    background: var(--dropdown); color: #fff; font-size: 7.5px; text-align: center;
  }
  .lang-menu div { height: 16px; line-height: 16px; margin-top: 3px; }
  .lang-menu div:first-child { border-bottom: 1px solid rgba(255,255,255,0.8); }
  .next-btn {
    left: 918px; top: 308px; width: 44px; height: 44px; border-radius: 50%;
    background: var(--next-btn); border: 1px solid #f2e5de;
  }
  .next-btn svg { position: absolute; left: 15px; top: 12px; }
</style>
</head>
<body>
<div class="page">
  <svg class="grid-lines" width="1021" height="572" viewBox="0 0 1021 572">
    <g stroke="var(--rule)" stroke-width="1" fill="none">
      <line x1="0" y1="61" x2="1021" y2="61"/>
      <line x1="0" y1="287" x2="1021" y2="287"/>
      <line x1="0" y1="482" x2="1021" y2="482"/>
      <line x1="574" y1="509" x2="574" y2="572"/>
      <line x1="855" y1="509" x2="855" y2="572"/>
      <line x1="195" y1="560" x2="195" y2="572"/>
      <circle cx="85" cy="405" r="85"/>
    </g>
  </svg>

  <div class="abs menu-panel" role="img" aria-label="Blurred black and white model portrait behind the menu"></div>
  <div class="abs menu-fade"></div>

  <svg class="abs close-btn" viewBox="0 0 14 14" aria-label="Close menu">
    <path d="M1 1L13 13M13 1L1 13" stroke="var(--brand)" stroke-width="1.6"/>
  </svg>

  <nav class="abs city-list">
    <span>LONDON</span><span>PARIS</span><span class="current">ISTANBUL</span><span>MILAN</span><span>ATHENS</span><span>DUBAI</span>
  </nav>

  <ul class="abs main-menu">
    <li style="top:72px">WOMEN</li>
    <li class="active" style="top:104px"><span>MEN</span></li>
    <li style="top:145px">IN TOWN</li>
    <li style="top:178px">LUNA MOTHER AGENCY</li>
    <li style="top:213px">BE A MODEL</li>
    <li style="top:248px">CONTACT</li>
    <li style="top:284px">ABOUT</li>
  </ul>

  <div class="abs brand">LUNA</div>
  <div class="abs top-nav" style="left:611px">BE A MODEL</div>
  <div class="abs top-nav" style="left:694px">ABOUT</div>
  <div class="abs top-nav" style="left:757px">CONTACT</div>
  <div class="abs top-nav" style="left:834px">LANGUAGE</div>
  <div class="abs search">
    <svg width="8" height="8" viewBox="0 0 8 8"><circle cx="3.2" cy="3.2" r="2.4" stroke="var(--brand)" fill="none"/><path d="M5 5L7.5 7.5" stroke="var(--brand)"/></svg>
  </div>

  <div class="abs photo-mono" role="img" aria-label="Black and white photo of a curly-haired model sitting on rocks by the sea"></div>
  <div class="abs photo-colour" role="img" aria-label="Colour photo of a red-haired model in a green embroidered jacket against an orange backdrop"></div>

  <div class="abs lang-menu"><div>ENGLISH</div><div>TURKISH</div></div>

  <div class="abs next-btn" aria-label="Next slide">
    <svg width="14" height="20" viewBox="0 0 14 20"><path d="M3 2L11 10L3 18" stroke="#5a4a44" stroke-width="2" fill="none"/></svg>
  </div>
</div>
</body>
</html>
```